iOS developer portal page

We need a web design for a company based in Beijing called BrightNook. Our company develops an SDK used by iOS developers making children's educational apps. The SDK provides cross-promotional marketing, user analytics, teacher feedback and activities, and parent reports for developers who implement it.
Our company offers a product that benefits parents and developers, however the design we need is in regard to the landing page for developers using our product.Developers using our SDK are mostly based in the USA and develop apps for the USA Orchard Tunebox store.
There is an included wireframe for the first design idea. Design comps can be similar or different from the wireframe, however it should be considered as a good starting point for the final design.
Updates
Thank you for the design submissions. We are currently reviewing the designs internally and will notify all designers once a decision has been reached.
Kind regards,
Merrick
Project Deadline Extended
Reason: The deadline is being extended by one day so it will be closed at the end of the business week. Thank you.
Target Market(s)
iOS Developers for Children's education apps
Industry/Entity Type
It Company
Look and feel
Each slider illustrates characteristics of the customer's brand and the style your logo design should communicate.

```html
<!DOCTYPE html>
<html lang="en">
<head>
<meta charset="utf-8">
<title>BrightNook – SDK for Children's Education Apps</title>
<link rel="stylesheet" href="https://fonts.googleapis.com/css2?family=Questrial&family=Arimo:wght@400;700&display=swap">
<style>
  :root {
    --header-brown: #463731;
    --nav-tan: #8a7a68;
    --nav-tan-light: #a39583;
    --hero-bg: #efeeed;
    --ink: #222222;
    --ink-grey: #5a5a5a;
    --green-top: #2c8a2e;
    --green-bottom: #6aa84a;
    --card: #ffffff;
    --feature-brown: #6a4a33;
    --feature-ink: #2e1f14;
    --feature-rule: #54392a;
    --accent-green: #5fb51e;
    --signup-dark: #3f7d10;
    --button-blue: #2d8fd0;
    --button-blue-dark: #1867a6;
    --link-blue: #1a62c4;
    --copy-brown: #6b4a2c;
    --footer-brown: #463731;
    --footer-ink: #9a8d84;
    --login-grey: #6d605a;
    --social: #5c7fa8;
    --art-neutral-light: #f1f0ee;
    --art-neutral-dark: #d9d6d2;
  }
  * { box-sizing: border-box; margin: 0; padding: 0; }
  html, body { width: 1099px; height: 1200px; overflow: hidden; }
  body { font-family: "Arimo", Arial, sans-serif; color: var(--ink); background: #fff; }
  .page { position: relative; width: 1099px; height: 1200px; overflow: hidden;
          background: linear-gradient(180deg, var(--green-top) 332px, #3f9538 420px, var(--green-bottom) 900px); }
  .abs { position: absolute; }

  /* Header */
  .topbar { left: 0; top: 0; width: 1099px; height: 81px; background: var(--header-brown); }
  .navband { left: 0; top: 81px; width: 1099px; height: 30px;
             background: linear-gradient(180deg, var(--nav-tan-light), var(--nav-tan)); }
  .brand { left: 16px; top: 28px; display: flex; align-items: center; gap: 10px;
           font-family: "Questrial", sans-serif; font-size: 38px; color: var(--accent-green); }
  .brand-dot { width: 18px; height: 18px; border-radius: 50%; background: var(--accent-green); }
  .social { left: 775px; top: 3px; display: flex; gap: 5px; }
  .social span { width: 26px; height: 27px; border-radius: 4px; background: var(--social); display: block; }
  .social span:nth-child(3), .social span:nth-child(5) { background: #d9822b; }
  .social span:nth-child(4) { background: #6a3d8a; }
  .social span:nth-child(6) { background: #b73a2e; }
  .login { left: 981px; top: 0; width: 109px; height: 25px; background: var(--login-grey);
           border-radius: 0 0 4px 4px; color: #eee; font-size: 15px; padding: 4px 0 0 16px; }
  .login svg { position: absolute; right: 10px; top: 10px; }
  .nav { left: 330px; top: 81px; height: 30px; display: flex; list-style: none; }
  .nav li { height: 30px; line-height: 30px; padding: 0 27px; color: #3b2e28; font-size: 15px;
            border-right: 1px solid #6d5f51; }
  .nav li:first-child { color: #fff; }
  .search { left: 866px; top: 84px; width: 230px; height: 25px; background: #fff; border: 1px solid #ccc; }
  .search svg { position: absolute; left: 6px; top: 5px; }

  /* Hero */
  .hero { left: 0; top: 111px; width: 1099px; height: 221px; background: var(--hero-bg); }
  .hero-photo { left: 676px; top: 111px; width: 423px; height: 221px;
                background: linear-gradient(100deg, #e9e6e2 0%, #c9b6a2 35%, #3a3638 70%, #2a2628 100%); }
  .hero-title { left: 20px; top: 132px; font-family: "Questrial", sans-serif; font-size: 41px; color: var(--ink); font-weight: 400; }
  .hero-title strong { font-family: "Arimo", sans-serif; font-weight: 700; color: var(--ink-grey); font-size: 39px; }
  .hero-copy { left: 20px; top: 196px; width: 650px; font-size: 12.9px; line-height: 16px; color: #111; }
  .signup { left: 555px; top: 296px; width: 140px; height: 29px; border-radius: 6px;
            background: linear-gradient(180deg, #7cc32a, #4d9a12); border: 2px solid var(--signup-dark);
            color: #fff; font-weight: 700; font-size: 20px; text-align: center; line-height: 25px; }

  /* Cards */
  .card { background: var(--card); border-radius: 6px; }
  .features { left: 15px; top: 352px; width: 1065px; height: 343px; }
  .section-title { font-family: "Questrial", sans-serif; font-size: 20px; color: var(--ink); font-weight: 400; }
  .features-title { left: 33px; top: 368px; }
  .feature-art { top: 420px; height: 103px; border-radius: 4px;
                 background: linear-gradient(160deg, var(--art-neutral-light), var(--art-neutral-dark)); }
  .feature-panel { left: 29px; top: 533px; width: 1042px; height: 253px; background: var(--feature-brown); border-radius: 5px; }
  .feature-rule { top: 541px; width: 1px; height: 237px; background: var(--feature-rule); }
  .feature { top: 550px; width: 200px; }
  .feature h3 { font-family: "Questrial", sans-serif; font-weight: 400; color: #fff; font-size: 16px; line-height: 19px; margin-bottom: 7px; width: 170px; }
  .feature p { font-size: 12.7px; line-height: 16px; color: var(--feature-ink); width: 196px; }
  .learn-more { width: 102px; height: 19px; border-radius: 10px;
                background: linear-gradient(180deg, #5fb5e8, var(--button-blue) 55%, var(--button-blue-dark));
                color: #fff; font-size: 9.5px; font-weight: 700; letter-spacing: .3px; line-height: 19px; padding-left: 11px; top: 755px; }
  .learn-more svg { position: absolute; right: 10px; top: 5px; }

  .press { left: 31px; top: 813px; width: 481px; height: 168px; }
  .press-art { left: 68px; top: 825px; width: 80px; height: 145px; border-radius: 40px 40px 12px 12px;
               background: linear-gradient(180deg, #e2d3bf, #b9a58c 65%, #7a7a7a); }
  .press-title { left: 168px; top: 828px; font-size: 21px; }
  .press-copy { left: 173px; top: 866px; width: 305px; font-size: 12.9px; line-height: 16px; color: var(--copy-brown); }

  .testimonials { left: 589px; top: 813px; width: 482px; height: 168px; }
  .testimonials-title { left: 605px; top: 821px; font-size: 21px; }
  .quote-mark { font-family: Georgia, serif; font-size: 34px; font-weight: 700; color: #222; line-height: 1; }
  .testimonial-copy { left: 626px; top: 862px; width: 408px; font-size: 12.9px; line-height: 16px; color: #333; }
  .testimonial-by { left: 969px; top: 948px; font-size: 12.5px; color: #333; }

  .releases { left: 31px; top: 1001px; width: 1040px; height: 153px; }
  .releases-title { left: 45px; top: 1014px; font-size: 21px; }
  .releases-rule { left: 535px; top: 1010px; width: 1px; height: 135px; background: #e2e2e2; }
  .app-icon { top: 1052px; width: 75px; height: 75px; border: 1px solid #ccc; border-radius: 4px; background: #fff; padding: 5px; }
  .app-icon div { width: 100%; height: 100%; border-radius: 3px; }
  .app-name { top: 1062px; font-size: 15px; font-weight: 700; color: var(--link-blue); text-decoration: underline; letter-spacing: .3px; }
  .app-by { top: 1087px; font-size: 11.5px; color: #888; }
  .app-by span { color: var(--link-blue); }
  .app-enabled { top: 1103px; font-size: 11.5px; color: #2f9a12; }
  .price { top: 1066px; width: 60px; text-align: center; font-size: 16px; font-weight: 700; color: #111; }
  .store-badge { top: 1093px; width: 50px; height: 18px; border-radius: 3px; background: linear-gradient(180deg, #9a9a9a, #5c5c5c); }

  /* Footer */
  .footer { left: 0; top: 1160px; width: 1099px; height: 40px; background: var(--footer-brown); }
  .copyright { left: 40px; top: 1176px; font-size: 10.5px; color: #6f5f55; }
  .footer-links { right: 34px; top: 1175px; display: flex; list-style: none; font-size: 11.5px; color: var(--footer-ink); }
  .footer-links li { padding: 0 12px; border-left: 1px solid #7a6c62; line-height: 13px; }
  .footer-links li:first-child { border-left: none; }
</style>
</head>
<body>
<div class="page">

  <!-- Header -->
  <header>
    <div class="abs topbar"></div>
    <div class="abs navband"></div>
    <div class="abs brand"><span class="brand-dot"></span>BrightNook</div>
    <div class="abs social" aria-label="Social links"><span></span><span></span><span></span><span></span><span></span><span></span></div>
    <div class="abs login">Login
      <svg width="8" height="5" viewBox="0 0 8 5"><path d="M0 0h8L4 5z" fill="#ddd"/></svg>
    </div>
    <ul class="abs nav">
      <li>Home</li><li>About us</li><li>News</li><li>Support</li><li>Contact</li>
    </ul>
    <div class="abs search">
      <svg width="14" height="14" viewBox="0 0 14 14"><circle cx="5.5" cy="5.5" r="4" fill="none" stroke="#333" stroke-width="2"/><path d="M8.5 8.5L13 13" stroke="#333" stroke-width="2.4"/></svg>
    </div>
  </header>

  <!-- Hero -->
  <section>
    <div class="abs hero"></div>
    <div class="abs hero-photo" role="img" aria-label="Photo of a mother and child smiling at a laptop beside a teddy bear"></div>
    <h1 class="abs hero-title">Make your Apps <strong>IRRESISTABLE</strong></h1>
    <p class="abs hero-copy">Lorem ipsum dolor sit amet, consectetuer adipiscing elit, sed diam nonummy nibh euismod tincidunt ut laoreet dolore magna aliquam erat volutpat. Ut wisi enim ad minim veniam, quis nostrud exerci tation ullamcorper suscipit lobortis nisl ut aliquip ex ea commodo consequat. Duis autem vel eum iriure dolor in hendrerit in vulputate velit esse molestie consequat, vel illum dolore eu feugiat nulla facilisis at vero eros et accumsan et iusto odio dignissim qui blandit praesent luptatum zzril delenit augue duis dolore te feugait nulla facilisi.</p>
    <div class="abs signup">Signup</div>
  </section>

  <!-- Features -->
  <section>
    <div class="abs card features"></div>
    <h2 class="abs section-title features-title">Enable these great features in minutes</h2>
    <div class="abs feature-art" style="left:65px;width:160px;" role="img" aria-label="Illustration of a figure ticking a checklist"></div>
    <div class="abs feature-art" style="left:325px;width:100px;" role="img" aria-label="Illustration of a ladder leaning on stacked toy blocks"></div>
    <div class="abs feature-art" style="left:582px;width:168px;top:470px;height:53px;background:linear-gradient(90deg,#f6c25a,#f3ae3a);" role="img" aria-label="Illustration of a row of five gold stars"></div>
    <div class="abs feature-art" style="left:885px;width:110px;" role="img" aria-label="Illustration of a cluster of coloured cubes"></div>

    <div class="abs feature-panel"></div>
    <div class="abs feature-rule" style="left:270px"></div>
    <div class="abs feature-rule" style="left:536px"></div>
    <div class="abs feature-rule" style="left:811px"></div>

    <div class="abs feature" style="left:53px"><h3>Parent Report</h3><p>Lorem ipsum dolor sit amet, consectetuer adipiscing elit, sed diam nonummy nibh euismod tincidunt ut laoreet dolore magna aliquam erat volutpat. Ut wisi enim ad minim veniam, quis nostrud exerci tation ullamcorper suscipit lobortis nisl ut aliquip ex ea commodo consequat.</p></div>
    <div class="abs feature" style="left:307px"><h3>Cross - Promotinal Marketing</h3><p>Lorem ipsum dolor sit amet, consectetuer adipiscing elit, sed diam nonummy nibh euismod tincidunt ut laoreet dolore magna aliquam erat volutpat. Ut wisi enim ad minim veniam, quis nostrud exerci tation ullamcorper suscipit lobortis nisl ut aliquip ex ea commodo consequat.</p></div>
    <div class="abs feature" style="left:573px"><h3>Teacher Feedback &amp; Activities</h3><p>Lorem ipsum dolor sit amet, consectetuer adipiscing elit, sed diam nonummy nibh euismod tincidunt ut laoreet dolore magna aliquam erat volutpat. Ut wisi enim ad minim veniam, quis nostrud exerci tation ullamcorper suscipit lobortis nisl ut aliquip ex ea commodo consequat.</p></div>
    <div class="abs feature" style="left:838px"><h3>User Analytics</h3><p>Lorem ipsum dolor sit amet, consectetuer adipiscing elit, sed diam nonummy nibh euismod tincidunt ut laoreet dolore magna aliquam erat volutpat. Ut wisi enim ad minim veniam, quis nostrud exerci tation ullamcorper suscipit lobortis nisl ut aliquip ex ea commodo consequat.</p></div>

    <div class="abs learn-more" style="left:150px">LEARN MORE<svg width="8" height="9" viewBox="0 0 8 9"><path d="M0 0l8 4.5L0 9z" fill="#fff"/></svg></div>
    <div class="abs learn-more" style="left:415px">LEARN MORE<svg width="8" height="9" viewBox="0 0 8 9"><path d="M0 0l8 4.5L0 9z" fill="#fff"/></svg></div>
    <div class="abs learn-more" style="left:691px">LEARN MORE<svg width="8" height="9" viewBox="0 0 8 9"><path d="M0 0l8 4.5L0 9z" fill="#fff"/></svg></div>
    <div class="abs learn-more" style="left:949px">LEARN MORE<svg width="8" height="9" viewBox="0 0 8 9"><path d="M0 0l8 4.5L0 9z" fill="#fff"/></svg></div>
  </section>

  <!-- Press -->
  <section>
    <div class="abs card press"></div>
    <div class="abs press-art" role="img" aria-label="Illustration of a light bulb shaped like a brain"></div>
    <h2 class="abs section-title press-title">BrightNook Featured in ByteWire</h2>
    <p class="abs press-copy">Lorem ipsum dolor sit amet, consectetuer adipiscing elit, sed diam nonummy nibh euismod tincidunt ut laoreet dolore magna aliquam erat volutpat. Ut wisi enim ad minim veniam, quis nostrud exerci tation ullamcorper suscipit lobortis nisl ut aliquip ex ea commodo consequat.</p>
  </section>

  <!-- Testimonials -->
  <section>
    <div class="abs card testimonials"></div>
    <h2 class="abs section-title testimonials-title">Testimonials</h2>
    <span class="abs quote-mark" style="left:602px;top:856px">&ldquo;</span>
    <p class="abs testimonial-copy">Lorem ipsum dolor sit amet, consectetuer adipiscing elit, sed diam nonummy nibh euismod tincidunt ut laoreet dolore magna aliquam erat volutpat. Ut wisi enim ad minim veniam, quis nostrud exerci tation ullamcorper suscipit lobortis nisl ut aliquip ex ea commodo consequat.</p>
    <span class="abs quote-mark" style="left:1040px;top:910px">&rdquo;</span>
    <p class="abs testimonial-by">- client one</p>
  </section>

  <!-- Recent releases -->
  <section>
    <div class="abs card releases"></div>
    <h2 class="abs section-title releases-title">Recent Releases</h2>
    <div class="abs releases-rule"></div>

    <div class="abs app-icon" style="left:58px"><div role="img" aria-label="App icon with colourful flash card artwork" style="background:linear-gradient(135deg,#7cc8e8,#f2d873);"></div></div>
    <p class="abs app-name" style="left:144px">Pebblepop Super Flash Cards</p>
    <p class="abs app-by" style="left:144px">by <span>Tidewell Soft LLP</span></p>
    <p class="abs app-enabled" style="left:144px">BrightNook-Enabled!</p>
    <p class="abs price" style="left:408px">$0.99</p>
    <div class="abs store-badge" style="left:413px"></div>

    <div class="abs app-icon" style="left:616px"><div role="img" aria-label="App icon with fruit and number artwork" style="background:linear-gradient(135deg,#f4b74a,#e9793a);"></div></div>
    <p class="abs app-name" style="left:702px">Sunny Sprouts 123</p>
    <p class="abs app-by" style="left:702px">by <span>TaleSprout</span></p>
    <p class="abs app-enabled" style="left:702px">BrightNook-Enabled!</p>
    <p class="abs price" style="left:965px">Free</p>
    <div class="abs store-badge" style="left:970px"></div>
  </section>

  <!-- Footer -->
  <footer>
    <div class="abs footer"></div>
    <p class="abs copyright">Copyright 2011 © BrightNook All rights reserved.</p>
    <ul class="abs footer-links">
      <li>App Reviews</li><li>Developers</li><li>About Us</li><li>Contact</li><li>Terms of Use</li><li>Privacy Policy</li>
    </ul>
  </footer>

</div>
</body>
</html>
```